coralridge studio business card

Architectural firm business card

Please note:

corporate colour black+yellow are the only elements to be kept.
NO OTHER ELEMENT TO BE REUSED FROM PREVIOUS BUSINESS CARD.
Thank you.

Dear Everyone,

Thank you for your participation. I have upload the KVLT+ logo again for incoporate in the card. in tif and pdf format.

Thank you 

I keep getting request for the logo file. Does everyone has the same problem?

I cannot do much, because the file is upload to the website server. I can't seem to see it either.

The logo file is now working. Please download. I check it myself. Thank you everyone.

Dear All,

Thank you for all the hard work. There are a lot of great work. Due to current commitment with work, I am unable to review them just yet. I will do so next week and advise everyone also. Thank you again. Best regards

Dear All,

Thank you for your participation. There are a lot of good design. Unfortunately, I can only select one. All the best. This is definitely a good crowd to work with. Thank you everyone again.

Best regards

Target Market(s)

Corporate, commercial and institutional projects only

Industry/Entity Type

Business

Requirements
Must have
• elegant simple
double sided with coating
Member of Southern Guild of Draftsmen (logo only)
corporate colour black and

LOGO FILE UPLOADED
Should not have
• should not be the same as current business card.
upload for reference information only.
font sans serif preferred.

```html
<!DOCTYPE html>
<html lang="en">
<head>
<meta charset="utf-8">
<title>coralridge studio business card</title>
<link rel="stylesheet" href="https://fonts.googleapis.com/css2?family=Oswald:wght@400;500&family=Open+Sans:wght@400;600&family=Cormorant+SC:wght@600&display=swap">
<style>
  :root {
    --stage: #e9e6e1;
    --brown-deep: #3a2a12;
    --brown-mid: #5e4620;
    --brown-light: #8c7a5c;
    --taupe: #7a6b58;
    --beige: #d9d2c6;
    --paper: #ffffff;
    --orange: #f28a2e;
    --orange-dark: #c9641a;
    --ink-light: #f3ede4;
  }
  * { margin: 0; padding: 0; box-sizing: border-box; }
  html, body { width: 1200px; height: 646px; overflow: hidden; }
  body { background: var(--stage); position: relative; font-family: "Open Sans", sans-serif; }

  .card {
    position: absolute; top: 158px; width: 540px; height: 330px;
    box-shadow: 0 10px 30px rgba(0,0,0,.25); overflow: hidden;
  }
  .card--front {
    left: 40px;
    background: radial-gradient(ellipse 60% 75% at 42% 22%, var(--brown-light) 0%, var(--brown-mid) 55%, var(--brown-deep) 100%);
  }
  .card--back { left: 620px; background: linear-gradient(120deg, var(--brown-mid) 0%, var(--brown-deep) 100%); }

  /* front */
  .front-brand { position: absolute; left: 0; right: 0; top: 82px; text-align: center; }
  .wordmark {
    display: inline-flex; align-items: center; gap: 10px;
    font-family: "Oswald", sans-serif; font-weight: 400; letter-spacing: 2px;
  }
  .wordmark__square { width: 18px; height: 18px; }
  .front-brand .wordmark { font-size: 30px; color: var(--beige); }
  .front-brand .wordmark__square { background: var(--beige); }
  .front-web {
    margin-top: 34px; font-family: "Oswald", sans-serif; font-size: 17px;
    letter-spacing: 1px; color: var(--ink-light);
  }
  .front-tagline { margin-top: 4px; font-size: 12px; color: var(--beige); letter-spacing: .5px; }
  .member-badge {
    position: absolute; right: 26px; top: 22px; width: 34px; height: 40px;
    background: var(--beige); border: 1px solid #b9b0a2;
  }

  /* back */
  .back-panel {
    position: absolute; left: 0; top: 0; bottom: 0; width: 205px; background: var(--paper);
    display: flex; flex-direction: column; justify-content: flex-end; padding: 0 18px 46px;
  }
  .back-panel .wordmark { font-size: 20px; color: var(--taupe); flex-wrap: nowrap; }
  .back-panel .wordmark__square { background: var(--taupe); width: 14px; height: 14px; }
  .back-web { margin-top: 6px; font-size: 9px; color: var(--taupe); }

  .name-ribbon {
    position: absolute; left: 190px; top: 46px; width: 330px; height: 34px;
    background: var(--orange); display: flex; align-items: center; padding-left: 24px;
    font-family: "Oswald", sans-serif; font-size: 19px; color: var(--paper); letter-spacing: .5px;
  }
  .name-ribbon__post { font-size: 15px; margin-left: 6px; }
  .name-ribbon__tail {
    position: absolute; left: 205px; top: 80px; width: 150px; height: 12px;
  }
  .role {
    position: absolute; left: 360px; top: 92px;
    font-family: "Cormorant SC", serif; font-weight: 600; font-size: 15px; color: var(--ink-light);
  }
  .contacts {
    position: absolute; left: 270px; top: 140px; display: grid;
    grid-template-columns: 62px auto; column-gap: 8px; row-gap: 4px; font-size: 11px;
  }
  .contacts dt { color: var(--orange); text-align: right; text-transform: uppercase; font-weight: 600; }
  .contacts dd { color: var(--ink-light); }
</style>
</head>
<body>
  <section class="card card--front" aria-label="Card front">
    <div class="member-badge" aria-label="Southern Guild of Draftsmen member badge"></div>
    <div class="front-brand">
      <div class="wordmark"><span class="wordmark__square"></span>CORALRIDGE STUDIO</div>
      <p class="front-web">WWW.CORALRIDGESTUDIO.COM.AU</p>
      <p class="front-tagline">architects · urban designers · project managers</p>
    </div>
  </section>

  <section class="card card--back" aria-label="Card back">
    <div class="back-panel">
      <div class="wordmark"><span class="wordmark__square"></span>CORALRIDGE STUDIO</div>
      <p class="back-web">www.coralridgestudio.com.au</p>
    </div>

    <div class="name-ribbon">ELLIS MORENO<span class="name-ribbon__post">kvlt.gpm</span></div>
    <svg class="name-ribbon__tail" viewBox="0 0 150 12" aria-hidden="true">
      <polygon points="0,0 150,0 140,12 0,12" fill="var(--orange-dark)"/>
    </svg>
    <p class="role">Director</p>

    <dl class="contacts">
      <dt>Cell</dt><dd>0400 27 61 48</dd>
      <dt>Office</dt><dd>+612 9000 4172</dd>
      <dt>Fax</dt><dd>+612 9000 4173</dd>
      <dt>Email</dt><dd>mail@coralridgestudio.com.au</dd>
      <dt>Address</dt><dd>Alderwood House<br>12 Finch Lane<br>Kestrel Bay NSW 2999</dd>
    </dl>
  </section>
</body>
</html>
```